KWT Contracting services . Building and maintenance services, optic fibre installation

Business cards and logo design.I need a logo that I can use on business cards ,workwear and on my vehicles. I would like the KWT to be the main or larger text and contracting services to be the smaller or less important text.I like monograms, modern designs and repeating patterns symbols. I am also a Gemini and my favourite number is 22 so if this can be any inspiration to help with the design. Am thinking of the using German flag colours as a his is my family’s heritage. And the other 2 main colours I wear is black and white.But any ideas are appreciated.I do not need a design that is trade specific but a design that could be used for any business.

Target Market(s)

General public

Contact Information for Business Card

KWT Contracting Services ( front of business card)

(Back of business card)
Milo Brackwood
0471539264
Maintenance services
Optic fibre and data installation

Logo Text

Logo can just be pattern or monogram or incorporate KWT . I like the gemini star sign and the number 22

Colors
ec1f27
000000
fbee3e
ffffff

Requirements
Must have
• Logo and KWT Contracting Services on the front of business card
Nice to have
• Possible use of German flag colours.
• Modern design.
• Design to be able to be used on black or white background as I want to put it on clothing

```html
<!DOCTYPE html>
<html lang="en">
<head>
<meta charset="utf-8">
<title>KWT Contracting Services – Business Cards</title>
<link href="https://fonts.googleapis.com/css2?family=Oxanium:wght@600&family=Lato:ital,wght@0,400;1,400&display=swap" rel="stylesheet">
<style>
  :root {
    --page: #ffffff;
    --card: #17181a;
    --yellow: #fed400;
    --red: #fd0606;
  }
  * { margin: 0; padding: 0; box-sizing: border-box; }
  html, body { width: 1200px; height: 1080px; overflow: hidden; background: var(--page); }
  .canvas { position: relative; width: 1200px; height: 1080px; }

  .card {
    position: absolute;
    background: var(--card);
    border-radius: 26px;
    color: var(--yellow);
    text-align: center;
  }
  .card--front { left: 288px; top: 35px; width: 630px; height: 344px; }
  .card--back  { left: 412px; top: 434px; width: 398px; height: 592px; }

  .brand-name {
    position: absolute; left: 0; right: 0;
    font-family: "Oxanium", sans-serif;
    font-weight: 600;
    color: var(--yellow);
    line-height: 1;
    letter-spacing: 0.02em;
  }
  .card--front .brand-name { top: 48px; font-size: 170px; }
  .card--back .brand-name  { top: 40px; font-size: 132px; }

  .brand-tagline {
    position: absolute; left: 0; right: 0;
    font-family: "Oxanium", sans-serif;
    font-weight: 600;
    line-height: 1;
    letter-spacing: 0.04em;
  }
  .card--front .brand-tagline { top: 248px; font-size: 31px; }
  .card--back .brand-tagline  { top: 180px; font-size: 23.5px; }

  .contact-name {
    position: absolute; left: 0; right: 0; top: 270px;
    font-family: "Lato", sans-serif;
    font-size: 44px;
    line-height: 46px;
    letter-spacing: 0.01em;
  }
  .contact-phone {
    position: absolute; left: 0; right: 0; top: 374px;
    display: flex; justify-content: center; align-items: center; gap: 14px;
    font-family: "Lato", sans-serif;
    font-size: 30px;
    letter-spacing: 0.04em;
  }
  .contact-phone svg { width: 30px; height: 30px; }

  .service-list {
    position: absolute; left: 0; right: 0; top: 502px;
    list-style: none;
    font-family: "Lato", sans-serif;
    font-style: italic;
    line-height: 1;
  }
  .service-list li:first-child { font-size: 19px; margin-bottom: 11px; }
  .service-list li:last-child  { font-size: 17px; }
</style>
</head>
<body>
<main class="canvas">
  <section class="card card--front" aria-label="Business card front">
    <div class="brand-name">KWT</div>
    <div class="brand-tagline">CONTRACTING SERVICES</div>
  </section>

  <section class="card card--back" aria-label="Business card back">
    <div class="brand-name">KWT</div>
    <div class="brand-tagline">CONTRACTING SERVICES</div>
    <h1 class="contact-name">MILO<br>BRACKWOOD</h1>
    <p class="contact-phone">
      <svg viewBox="0 0 24 24" aria-hidden="true">
        <path fill="#fd0606" d="M5 21c-1.2-1.2-1.2-2.6-.4-3.6l2-2.2c.6-.6 1.4-.6 2 0l1 1c2.4-1.2 4-2.8 5.2-5.2l-1-1c-.6-.6-.6-1.4 0-2l2.2-2c1-.8 2.4-.8 3.6.4l-.9 1c-.5-.4-1-.4-1.4 0l-1.6 1.5 1.2 1.2c-1.6 3.6-4 6-7.6 7.6l-1.2-1.2-1.5 1.6c-.4.4-.4.9 0 1.4z"/>
      </svg>
      <span>047 153 92 64</span>
    </p>
    <ul class="service-list">
      <li>-MAITENANCE SERVICES</li>
      <li>-OPTIC FIBRE AND DATA INSTALATION</li>
    </ul>
  </section>
</main>
</body>
</html>
```